Custom Office Whiteboard for Staff

I need a custom whiteboard layout design. All fields are contained in the attached images along with artwork requirements including required bleed. Size will be 1200mm x 900mm.

Feel free to make is more visually appealing than this draft.

Use colors blue, black and white to keep company feel.

Font styles to use
Sans Serif

Colors
ffffff
000000
33a6d7

```html
<!DOCTYPE html>
<html lang="en">
<head>
<meta charset="utf-8">
<title>Skyward Ballooning – Staff Whiteboard</title>
<link href="https://fonts.googleapis.com/css2?family=Roboto:wght@400;500;700&family=Roboto+Condensed:wght@500;700&display=swap" rel="stylesheet">
<style>
  :root{
    --brand-blue:#33a6d7;
    --brand-blue-deep:#1ea0e0;
    --footer-light:#3fc3f2;
    --row-light:#f3f5f5;
    --row-tint:#e2f6fd;
    --grid-line:#a7b3b8;
    --ink:#000000;
    --paper:#ffffff;
  }
  *{box-sizing:border-box;margin:0;padding:0}
  html,body{width:900px;height:1200px;overflow:hidden;background:var(--paper)}
  body{position:relative;font-family:"Roboto",Arial,sans-serif;color:var(--ink)}

  .brand{position:absolute;left:0;top:72px;width:900px;display:flex;justify-content:center;align-items:center;gap:14px}
  .brand-dot{width:30px;height:30px;border-radius:50%;background:var(--brand-blue)}
  .brand-name{font-family:"Roboto",Arial,sans-serif;font-weight:700;font-size:40px;color:var(--ink);letter-spacing:1px}

  table{border-collapse:collapse;table-layout:fixed;position:absolute}
  td,th{border:1.5px solid var(--grid-line);text-align:center;vertical-align:middle;overflow:hidden;white-space:nowrap}
  tbody tr:nth-child(odd) td{background:var(--row-light)}
  tbody tr:nth-child(even) td{background:var(--row-tint)}
  .table-title th{background:var(--brand-blue);color:var(--paper);font-family:"Roboto Condensed",Arial,sans-serif;font-weight:700;border-color:var(--brand-blue)}
  .col-head th{background:var(--brand-blue);color:var(--paper);font-weight:400;border-color:#8fcbe6;border-top-color:var(--brand-blue)}

  .crew-table{left:61px;top:170px;width:773px}
  .crew-table .table-title th{height:32px;font-size:21px}
  .crew-table .col-head th{height:29px;font-size:9.5px;line-height:1.1;white-space:normal}
  .crew-table td{height:28.9px}

  .task-table{top:642px;width:256px}
  .task-table.six-month{left:61px}
  .task-table.twelve-month{left:324px}
  .task-table .table-title th,.schedule-table .table-title th{height:17px;font-size:11px;font-family:"Roboto",Arial,sans-serif;font-weight:500}
  .task-table .col-head th,.schedule-table .col-head th{height:22px;font-size:14px;font-family:"Roboto Condensed",Arial,sans-serif;font-weight:700}
  .task-table td,.schedule-table td{height:19.7px;font-size:9.5px}

  .schedule-table{left:61px;top:852px;width:517px}

  .notes-heading{position:absolute;left:688px;top:645px;font-size:22px;font-weight:700;text-decoration:underline;text-underline-offset:3px}

  .contact-band{position:absolute;left:60px;top:1065px;width:775px;height:78px;background:linear-gradient(90deg,var(--brand-blue-deep),var(--footer-light) 55%,var(--brand-blue-deep));color:var(--paper);font-size:14px}
  .contact-list{position:absolute;left:8px;top:12px;list-style:none}
  .contact-list li,.company-list li{display:flex;align-items:flex-start;gap:6px;height:19px}
  .contact-list li.phone{font-size:16px;font-weight:500}
  .company-list{position:absolute;left:412px;top:12px;list-style:none;line-height:1.2}
  .company-list li.address{height:39px}
  svg.icon{width:13px;height:13px;flex:none;margin-top:2px;fill:var(--ink)}
</style>
</head>
<body>
  <header class="brand">
    <span class="brand-dot"></span>
    <span class="brand-name">Skyward Ballooning</span>
  </header>

  <table class="crew-table">
    <colgroup>
      <col style="width:88px"><col style="width:87px"><col style="width:85px"><col style="width:86px"><col style="width:86px"><col style="width:86px"><col style="width:84px"><col style="width:86px"><col style="width:85px">
    </colgroup>
    <thead>
      <tr class="table-title"><th colspan="9">Flight/Ground Crew</th></tr>
      <tr class="col-head">
        <th>Crew name</th><th>License Class</th><th>Medical</th><th>BRF</th><th>Instructor Rating</th><th>CAO 20.11</th><th>DAMP</th><th>Maintenance Authority</th><th>ASIC</th>
      </tr>
    </thead>
    <tbody>
      <tr><td></td><td></td><td></td><td></td><td></td><td></td><td></td><td></td><td></td></tr>
      <tr><td></td><td></td><td></td><td></td><td></td><td></td><td></td><td></td><td></td></tr>
      <tr><td></td><td></td><td></td><td></td><td></td><td></td><td></td><td></td><td></td></tr>
      <tr><td></td><td></td><td></td><td></td><td></td><td></td><td></td><td></td><td></td></tr>
      <tr><td></td><td></td><td></td><td></td><td></td><td></td><td></td><td></td><td></td></tr>
      <tr><td></td><td></td><td></td><td></td><td></td><td></td><td></td><td></td><td></td></tr>
      <tr><td></td><td></td><td></td><td></td><td></td><td></td><td></td><td></td><td></td></tr>
      <tr><td></td><td></td><td></td><td></td><td></td><td></td><td></td><td></td><td></td></tr>
      <tr><td></td><td></td><td></td><td></td><td></td><td></td><td></td><td></td><td></td></tr>
      <tr><td></td><td></td><td></td><td></td><td></td><td></td><td></td><td></td><td></td></tr>
      <tr><td></td><td></td><td></td><td></td><td></td><td></td><td></td><td></td><td></td></tr>
      <tr><td></td><td></td><td></td><td></td><td></td><td></td><td></td><td></td><td></td></tr>
      <tr><td></td><td></td><td></td><td></td><td></td><td></td><td></td><td></td><td></td></tr>
    </tbody>
  </table>

  <table class="task-table six-month">
    <colgroup><col style="width:127px"><col style="width:129px"></colgroup>
    <thead>
      <tr class="table-title"><th colspan="2">6 Monthly Tasks</th></tr>
      <tr class="col-head"><th>Task</th><th>Due Date</th></tr>
    </thead>
    <tbody>
      <tr><td>Operations Manual</td><td></td></tr>
      <tr><td>Staff Meeting</td><td></td></tr>
      <tr><td>SMS&nbsp; Meeting</td><td></td></tr>
      <tr><td>Fire Extinguisher Inspection</td><td></td></tr>
      <tr><td>Flight Instrument Inspection</td><td></td></tr>
      <tr><td></td><td></td></tr>
      <tr><td></td><td></td></tr>
      <tr><td></td><td></td></tr>
    </tbody>
  </table>

  <table class="task-table twelve-month">
    <colgroup><col style="width:127px"><col style="width:129px"></colgroup>
    <thead>
      <tr class="table-title"><th colspan="2">12 Monthly Tasks</th></tr>
      <tr class="col-head"><th>Task</th><th>Due Date</th></tr>
    </thead>
    <tbody>
      <tr><td>COA Internal Audit</td><td></td></tr>
      <tr><td>SMS Audit</td><td></td></tr>
      <tr><td>Fatigue Training</td><td></td></tr>
      <tr><td>CAO 20.11</td><td></td></tr>
      <tr><td></td><td></td></tr>
      <tr><td></td><td></td></tr>
      <tr><td></td><td></td></tr>
      <tr><td></td><td></td></tr>
    </tbody>
  </table>

  <h2 class="notes-heading">NOTES</h2>

  <table class="schedule-table">
    <colgroup><col style="width:129px"><col style="width:131px"><col style="width:129px"><col style="width:128px"></colgroup>
    <thead>
      <tr class="table-title"><th colspan="4">Balloon Annual / Periodic Schedule</th></tr>
      <tr class="col-head"><th>Balloon</th><th>Type</th><th>Annual Date</th><th>Periodic Time</th></tr>
    </thead>
    <tbody>
      <tr><td>VH-SKA</td><td>Env D90</td><td></td><td></td></tr>
      <tr><td>VH-SKB</td><td>Env E180</td><td></td><td></td></tr>
      <tr><td>VH-SKC</td><td>Env E240</td><td></td><td></td></tr>
      <tr><td>VH-SKD</td><td>Env B400</td><td></td><td></td></tr>
      <tr><td>VH-SKE</td><td>Env G450</td><td></td><td></td></tr>
      <tr><td></td><td></td><td></td><td></td></tr>
      <tr><td></td><td></td><td></td><td></td></tr>
      <tr><td></td><td></td><td></td><td></td></tr>
    </tbody>
  </table>

  <footer class="contact-band">
    <ul class="contact-list">
      <li><svg class="icon" viewBox="0 0 16 16"><path d="M1 3h14v10H1z"/><path d="M1 3l7 6 7-6" fill="none" stroke="#3fc3f2" stroke-width="1.5"/></svg>info@skywardballooning.example</li>
      <li><svg class="icon" viewBox="0 0 16 16"><circle cx="8" cy="8" r="7"/><path d="M1 8h14M8 1c-3 3-3 11 0 14M8 1c3 3 3 11 0 14" fill="none" stroke="#3fc3f2" stroke-width="1.2"/></svg>www.skywardballooning.example</li>
      <li class="phone"><svg class="icon" viewBox="0 0 16 16"><circle cx="8" cy="8" r="7" fill="none" stroke="#000" stroke-width="1.5"/><path d="M5 4l2 0 .5 2-1 1c.5 1.2 1.3 2 2.5 2.5l1-1 2 .5v2c-4 .5-7.5-3-7-7z"/></svg>1300 555 012</li>
    </ul>
    <ul class="company-list">
      <li class="address"><svg class="icon" viewBox="0 0 16 16"><path d="M8 1a5 5 0 0 0-5 5c0 4 5 9 5 9s5-5 5-9a5 5 0 0 0-5-5z"/><circle cx="8" cy="6" r="2" fill="#3fc3f2"/></svg><span>Southern Envelope Pty Ltd T/A Skyward Ballooning<br>CASA AOC: S518204</span></li>
      <li><svg class="icon" viewBox="0 0 16 16"><circle cx="8" cy="7" r="6"/><path d="M5 11l-1 4 4-2 4 2-1-4z"/></svg>Certificate of Approval: 4819</li>
    </ul>
  </footer>
</body>
</html>
```